Laundry pickup and delivery flyer "Fold Harbor laundry"

I need a flyer "8.5"x11" that tells customers about our pickup and delivery laundry service. our website address is: www.foldharborlaundry.example The flyer should be front and back.

Font styles to use
Sans Serif

Colors
0094D4
00A9DD
6FCCEA
C7EBF8
E9F6FB

```html
<!DOCTYPE html>
<html lang="en">
<head>
<meta charset="utf-8">
<title>Fold Harbor laundry – Pickup &amp; Delivery Flyer</title>
<link rel="stylesheet" href="https://fonts.googleapis.com/css2?family=Baloo+2:wght@600;700;800&family=Fira+Sans:wght@800;900&display=swap">
<style>
  :root {
    --navy-bg: #071e38;
    --navy-ink: #0f3a68;
    --royal: #2f72b8;
    --blue: #0094d4;
    --sky: #00a9dd;
    --aqua: #6fccea;
    --mist: #c7ebf8;
    --foam: #e9f6fb;
    --white: #ffffff;
    --black: #0a0a0a;
  }
  * { box-sizing: border-box; margin: 0; padding: 0; }
  html, body { width: 1200px; height: 927px; overflow: hidden; background: var(--navy-bg); }
  .canvas { position: relative; width: 1200px; height: 927px; background: var(--navy-bg); }

  .flyer { position: absolute; width: 492px; height: 637px; background: var(--white); overflow: hidden; }
  .flyer--front { left: 87px; top: 76px; }
  .flyer--back { left: 606px; top: 204px; }
  .flyer__bands { position: absolute; inset: 0; width: 100%; height: 100%; }

  .splash-area { position: absolute; border-radius: 50%; }
  .flyer--front .splash-area {
    left: -60px; top: 300px; width: 420px; height: 330px;
    background: radial-gradient(closest-side, rgba(111,204,234,0.55), rgba(199,235,248,0.35) 60%, rgba(233,246,251,0) 100%);
  }
  .flyer--back .splash-area {
    left: 10px; top: 110px; width: 470px; height: 470px;
    background: radial-gradient(closest-side, rgba(255,255,255,0) 62%, rgba(199,235,248,0.7) 78%, rgba(111,204,234,0.55) 90%, rgba(233,246,251,0) 100%);
  }

  .brand { position: absolute; display: flex; align-items: center; gap: 8px;
    font-family: "Baloo 2", sans-serif; font-weight: 800; color: var(--royal); line-height: 1; white-space: nowrap; }
  .brand__dot { border-radius: 50%; background: var(--blue); flex: none; }
  .flyer--front .brand { left: 14px; top: 112px; font-size: 34px; }
  .flyer--front .brand__dot { width: 26px; height: 26px; }
  .flyer--back .brand { right: 28px; top: 58px; font-size: 21px; }
  .flyer--back .brand__dot { width: 16px; height: 16px; }

  .headline { position: absolute; font-family: "Fira Sans", sans-serif; font-weight: 800;
    color: var(--navy-ink); letter-spacing: 0.5px; white-space: nowrap; }
  .headline--service { left: 0; right: 0; top: 222px; text-align: center; font-size: 53px; line-height: 0.8; padding-left: 14px; }
  .headline--delivery { right: 46px; top: 446px; text-align: center; font-size: 57px; line-height: 0.72; }

  .reasons { position: absolute; left: 26px; top: 336px; width: 460px;
    font-family: "Baloo 2", sans-serif; font-weight: 700; color: var(--black); font-size: 14.2px; line-height: 17.5px; }
  .reasons__title { margin-left: 9px; font-size: 15px; font-weight: 800; }
  .reasons ul { list-style: none; }
  .reasons li { position: relative; padding-left: 9px; }
  .reasons li::before { content: ""; position: absolute; left: -3px; top: 6px; width: 6px; height: 6px; border-radius: 50%; background: var(--black); }

  .phone { position: absolute; left: 68px; top: 535px; display: flex; align-items: center; gap: 4px;
    font-family: "Fira Sans", sans-serif; font-weight: 900; font-size: 58px; color: var(--black); line-height: 1; letter-spacing: -0.5px; white-space: nowrap; }
  .phone svg { width: 42px; height: 42px; }

  .web-bar { position: absolute; left: 0; right: 0; bottom: 0; height: 39px; display: flex; align-items: center; justify-content: center;
    background: linear-gradient(90deg, rgba(15,58,104,0) 2%, var(--navy-ink) 16%, var(--navy-ink) 86%, rgba(15,58,104,0) 100%);
    font-family: "Baloo 2", sans-serif; font-weight: 800; color: var(--white); font-size: 19px; letter-spacing: 0.4px; }

  .pitch { position: absolute; left: 34px; width: 440px; top: 222px; text-align: center;
    font-family: "Baloo 2", sans-serif; font-weight: 700; color: var(--navy-ink); }
  .pitch__title { font-size: 26px; line-height: 1.25; font-weight: 800; }
  .pitch__body { font-size: 17.4px; line-height: 20.9px; }
  .pitch__name { font-size: 21px; font-weight: 800; }
</style>
</head>
<body>
<main class="canvas">

  <section class="flyer flyer--front">
    <svg class="flyer__bands" viewBox="0 0 492 637" aria-hidden="true">
      <defs>
        <linearGradient id="cornerFront" x1="0" y1="0" x2="1" y2="1">
          <stop offset="0" stop-color="#1c86c8"/>
          <stop offset="1" stop-color="#0094d4"/>
        </linearGradient>
      </defs>
      <path d="M150 0 H492 V345 C475 200 395 55 150 0 Z" fill="url(#cornerFront)"/>
      <path d="M132 0 C300 25 410 120 460 212 C420 140 330 50 190 0 Z" fill="var(--royal)"/>
    </svg>
    <div class="splash-area" role="img" aria-label="Water splash illustration"></div>

    <div class="brand"><span class="brand__dot"></span>Fold Harbor laundry</div>

    <h1 class="headline headline--service">LAUNDRY &amp;<br>DRY CLEANING</h1>

    <div class="reasons">
      <p class="reasons__title">WHY FOLD HARBOR?</p>
      <ul>
        <li>Our laundry professionals separate lights and darks to keep<br>your clothes looking great!</li>
        <li>Your items will never be washed with anyone else’s</li>
        <li>We use high quality detergents and eco friends chemicals</li>
        <li>No more Laundry day!</li>
      </ul>
    </div>

    <h2 class="headline headline--delivery">PICK UP<br>&amp; DELIVERY</h2>

    <div class="phone">
      <svg viewBox="0 0 42 42" aria-hidden="true">
        <circle cx="21" cy="21" r="20" fill="var(--black)"/>
        <path d="M13 11 l5 -1 l3 7 l-3 2 c1.5 3.5 3.5 5.5 7 7 l2 -3 l7 3 l-1 5 c-10 1 -21 -10 -20 -20 z" fill="var(--white)"/>
      </svg>
      <span>555-014-2290</span>
    </div>

    <div class="web-bar">WWW.FOLDHARBORLAUNDRY.EXAMPLE</div>
  </section>

  <section class="flyer flyer--back">
    <svg class="flyer__bands" viewBox="0 0 492 637" aria-hidden="true">
      <defs>
        <linearGradient id="cornerBack" x1="0" y1="0" x2="1" y2="1">
          <stop offset="0" stop-color="#1c86c8"/>
          <stop offset="1" stop-color="#0094d4"/>
        </linearGradient>
      </defs>
      <path d="M0 0 H290 C150 25 40 120 0 240 Z" fill="url(#cornerBack)"/>
      <path d="M282 0 C150 20 55 100 20 200 C60 110 140 40 240 0 Z" fill="var(--royal)"/>
      <path d="M492 340 C470 470 380 595 160 637 H492 Z" fill="url(#cornerBack)"/>
      <path d="M460 430 C430 530 340 615 160 637 H200 C340 605 420 530 460 430 Z" fill="var(--royal)"/>
    </svg>
    <div class="splash-area" role="img" aria-label="Water splash illustration around the text"></div>

    <div class="brand"><span class="brand__dot"></span>Fold Harbor laundry</div>

    <div class="pitch">
      <h2 class="pitch__title">Clean Clothes in a Few Clicks</h2>
      <p class="pitch__body"><span class="pitch__name">Fold Harbor</span> - Harbor City’s most<br>
        advanced and professional laundry<br>
        service - takes the work out of laundry day<br>
        with our instant pickup and delivery system.<br>
        With just a few clicks you can sign up for<br>
        service and schedule a pickup and delivery<br>
        time that fits your busy schedule. Your clothes<br>
        are expertly cleaned to your specifications,<br>
        folded, packaged, and delivered back to you<br>
        for easy storage.</p>
    </div>
  </section>

</main>
</body>
</html>
```